Lorvena Aesthetic Doctor

I require an elegant, luxurious looking business card for my aesthetic business. I am a doctor and that will set me aside from competitors. I am planning to provide home and spa based treatments to clients with high expectations. I have attached my logo.

```html
<!DOCTYPE html>
<html lang="en">
<head>
<meta charset="utf-8">
<title>Lorvena Aesthetic Doctor – Business Card</title>
<link rel="stylesheet" href="https://fonts.googleapis.com/css2?family=Josefin+Sans:wght@300;400&display=swap">
<style>
  :root {
    --stage: #e4e4e4;
    --card: #141414;
    --ink-light: #c9c9c9;
    --ink-soft: #a9a9a9;
    --accent: #6aaed6;
    --accent-deep: #3d7fb0;
    --pattern-a: #1b1b1b;
    --pattern-b: #262626;
  }
  * { margin: 0; padding: 0; box-sizing: border-box; }
  html, body { width: 1200px; height: 801px; overflow: hidden; }
  body {
    background: var(--stage);
    font-family: "Josefin Sans", sans-serif;
    position: relative;
  }
  .card {
    position: absolute;
    top: 246px;
    width: 540px;
    height: 309px;
    background: var(--card);
    box-shadow: 0 6px 18px rgba(0,0,0,.22);
    overflow: hidden;
  }
  .card--front { left: 40px; }
  .card--back { left: 620px; }

  /* Front */
  .brand {
    position: absolute;
    left: 32px;
    top: 38px;
    display: flex;
    align-items: center;
    gap: 14px;
    width: 300px;
  }
  .brand__circle {
    width: 64px; height: 64px;
    flex: none;
    border-radius: 50%;
    border: 2px solid var(--ink-soft);
  }
  .brand__name {
    color: var(--ink-light);
    font-weight: 300;
    font-size: 18px;
    letter-spacing: 2px;
    line-height: 1.3;
    text-transform: uppercase;
    white-space: nowrap;
  }
  .doctor {
    position: absolute;
    left: 32px;
    top: 152px;
    width: 280px;
  }
  .doctor__name {
    color: var(--accent);
    font-size: 17px;
    font-weight: 400;
    white-space: nowrap;
  }
  .doctor__title {
    color: var(--ink-soft);
    font-size: 11px;
    font-weight: 300;
    margin-top: 5px;
    white-space: nowrap;
  }
  .contacts {
    position: absolute;
    left: 32px;
    top: 204px;
    list-style: none;
  }
  .contacts li {
    display: flex;
    align-items: center;
    gap: 8px;
    color: var(--ink-soft);
    font-size: 11px;
    font-weight: 300;
    height: 19px;
  }
  .contacts svg { width: 13px; height: 13px; flex: none; }
  .services {
    position: absolute;
    right: 24px;
    top: 36px;
    list-style: none;
    text-align: right;
  }
  .services li {
    color: var(--ink-soft);
    font-size: 12px;
    font-weight: 300;
    height: 19px;
    display: flex;
    justify-content: flex-end;
    align-items: center;
    gap: 7px;
    white-space: nowrap;
  }
  .services li::after {
    content: "";
    width: 10px; height: 10px;
    border-radius: 50%;
    background: var(--accent);
  }
  .services li.no-dot::after { background: transparent; }

  /* Back */
  .pattern {
    position: absolute; inset: 0;
    background: radial-gradient(circle at 50% 50%, var(--pattern-b), var(--pattern-a) 75%);
  }
  .back-mark {
    position: absolute;
    left: 50%; top: 50%;
    transform: translate(-50%, -50%);
    display: flex; align-items: center; gap: 10px;
  }
  .back-mark__circle {
    width: 30px; height: 30px; border-radius: 50%;
    background: var(--accent-deep);
  }
  .back-mark__name {
    color: var(--accent);
    font-size: 13px;
    font-weight: 400;
    letter-spacing: 2px;
    text-transform: uppercase;
  }
</style>
</head>
<body>

<section class="card card--front">
  <div class="brand">
    <div class="brand__circle"></div>
    <div class="brand__name">Lorvena<br>Aesthetic Doctor</div>
  </div>

  <div class="doctor">
    <p class="doctor__name">Dr Elise Marrow MRCPCH MD</p>
    <p class="doctor__title">Australasian Diploma of Aesthetic Medicine</p>
  </div>

  <ul class="contacts">
    <li>
      <svg viewBox="0 0 14 14"><circle cx="7" cy="7" r="7" fill="#6aaed6"/><path d="M4.5 3.5h1.6l.7 1.8-1 .7a5 5 0 0 0 2.2 2.2l.7-1 1.8.7v1.6A1 1 0 0 1 9.5 10 6 6 0 0 1 3.5 4.5a1 1 0 0 1 1-1z" fill="#141414"/></svg>
      0800 555 014
    </li>
    <li>
      <svg viewBox="0 0 14 14"><circle cx="7" cy="7" r="7" fill="#6aaed6"/><rect x="3.5" y="4.5" width="7" height="5" fill="none" stroke="#141414" stroke-width="1"/><path d="M3.5 4.5 7 7.3l3.5-2.8" fill="none" stroke="#141414" stroke-width="1"/></svg>
      elise@lorvena.co.nz
    </li>
    <li>
      <svg viewBox="0 0 14 14"><circle cx="7" cy="7" r="7" fill="#6aaed6"/><circle cx="7" cy="7" r="3.5" fill="none" stroke="#141414"/><path d="M3.5 7h7M7 3.5v7" stroke="#141414" stroke-width=".8"/></svg>
      www.lorvena.co.nz
    </li>
    <li>
      <svg viewBox="0 0 14 14"><circle cx="7" cy="7" r="7" fill="#6aaed6"/></svg>
      /lorvenaaestheticdoctor
    </li>
  </ul>

  <ul class="services">
    <li>Dermal injectables</li>
    <li>Plasma facials</li>
    <li>Microneedling</li>
    <li>Skin boosters</li>
    <li>Excessive sweating</li>
    <li class="no-dot">Home and Spa Based Treatments</li>
  </ul>
</section>

<section class="card card--back">
  <div class="pattern" role="img" aria-label="Tonal embossed pattern of the brand symbol repeated across the card"></div>
  <div class="back-mark">
    <div class="back-mark__circle"></div>
    <span class="back-mark__name">Lorvena</span>
  </div>
</section>

</body>
</html>
```